We have a small 501C Non-Profit, called Youthful Hands. The non-profit was started by my son and his friends during the Gulf Oil Spill. We would like to update the website that currently sits on Namehaven.com. I'm not sure how we transfer over the domain or get them to host it with your new design. I've attached a link of the old site that we developed. We are open to any ideas regarding hosting.

We would basically like a look that is youth (teen, college age) oriented that will drive teens and donors to the site. Our goal is to get onto Brightwall Drives, get grants and make major donations with little to no administration expense. We will get sponsors to pay for the administration costs. So we will be looking for sponsors to support the overhead and 100% of donor money will go to causes important to teens.

http://www.youthfulhands.org

Target Market(s)

Teenagers and Individual Sponsors. Adults that want to help teens with an important cause.

Industry/Entity Type

Non-Profit

Requirements
Must have
• We are very open to ideas. It would be good to have a:

Home-with Mission Statement and Photos or Graphics
Donate-100% of Donations Go To Causes (with Coinpost Link)
Become A Sponsor-Insert Contact Information In This Section.
How It All Got Started -with info, articles, events, video, etc. from Gulf Oil Spill, Our Founder photo.
Contact-Change phone number to 555-318-2704. Keep e-mail and mailing the same.

You can use some existing photos from current site if you would like. All the Recent Event Photos, Founder Photo, 3 people holding check photo were all taken by me so there are no rights issues with those.

YH Mission Statement:

To demonstrate to the world that Youthful Hands about the environment, each other and world peace through fund raising and other philanthropic efforts.
Nice to have
• Youthful Hands Logo If Possible

Photo of 3 people, holding check, from existing home page in new History Section.

Kindly Paws League Story and Logo in History Section

WRT Video in History Section

Helpx9
http://www.helpx9.example/causes/teenager-starts-non-profit-to-raise-money-for-animals-victims-of-gulf-oil-spill.html
Should not have
• Delete Blog Section
Delete Founder Section
Delete Recent Events
Delete How To Get Involved

```html
<!DOCTYPE html>
<html lang="en">
<head>
<meta charset="utf-8">
<title>Youthful Hands</title>
<link rel="stylesheet" href="https://fonts.googleapis.com/css2?family=PT+Sans:wght@400;700&family=Open+Sans:wght@400;600&display=swap">
<style>
  :root {
    --ink: #222;
    --dark-panel: #1f1f1f;
    --orange: #f07d10;
    --orange-dark: #d96400;
    --blue: #0c5a9e;
    --blue-nav-top: #5f8dcc;
    --blue-nav-bottom: #3a67ab;
    --footer-blue: #0a58a0;
    --page-bg: #f3f3f3;
    --card-border: #e2e2e2;
    --white: #fff;
  }
  * { margin: 0; padding: 0; box-sizing: border-box; }
  html, body { width: 1200px; height: 975px; overflow: hidden; }
  body { position: relative; background: var(--page-bg); font-family: Arial, Helvetica, sans-serif; color: var(--ink); }
  .abs { position: absolute; }

  .site-header { left: 0; top: 0; width: 1200px; height: 100px; background: linear-gradient(#fff 0%, #fff 55%, #ececec 100%); border-top: 3px solid #333; }
  .brand { left: 128px; top: 30px; display: flex; align-items: center; gap: 14px; }
  .brand-name { font-family: "PT Sans", sans-serif; font-size: 40px; font-weight: 400; color: #1d1d1d; letter-spacing: 1px; }
  .brand-mark { width: 62px; height: 62px; border-radius: 50%; background: #3d6fb8; }
  .call-tab { left: 840px; top: 0; width: 252px; height: 42px; background: linear-gradient(#3a3a3a, #1c1c1c); border-radius: 0 0 12px 12px; display: flex; align-items: center; padding-left: 16px; gap: 8px; font-family: "Open Sans", sans-serif; }
  .call-icon { width: 24px; height: 24px; border-radius: 4px; background: #5c8fd0; display: flex; align-items: center; justify-content: center; }
  .call-label { color: #74a8e6; font-size: 15px; font-weight: 600; }
  .call-number { color: var(--white); font-size: 17px; }

  .main-nav { left: 0; top: 100px; width: 1200px; height: 34px; background: linear-gradient(var(--blue-nav-top), var(--blue-nav-bottom)); }
  .nav-link { position: absolute; top: 0; height: 34px; line-height: 36px; color: var(--white); font-family: "Open Sans", sans-serif; font-size: 12.5px; letter-spacing: .5px; }
  .nav-link.active { background: #111; top: -5px; height: 39px; line-height: 46px; padding: 0 14px; }
  .nav-sep { position: absolute; top: 9px; width: 1px; height: 20px; background: rgba(255,255,255,.5); }

  .content-bg { left: 12px; top: 134px; width: 1176px; height: 728px; background: #f8f8f8; }

  .hero { left: 146px; top: 148px; width: 928px; height: 369px; background: #efefef; border: 1px solid #ddd; }
  .hero-photo { left: 155px; top: 157px; width: 548px; height: 350px; background: linear-gradient(160deg, #c9b87a 0%, #8a8f78 30%, #e8e4dc 55%, #6e6a5f 100%); }
  .hero-caption { left: 155px; top: 450px; width: 548px; height: 57px; background: rgba(0,0,0,.72); color: var(--white); font-family: "Open Sans", sans-serif; font-size: 20.5px; line-height: 26px; padding: 2px 7px; }
  .hero-panel { left: 713px; top: 148px; width: 361px; height: 369px; background: var(--dark-panel); overflow: hidden; }
  .hero-title { position: absolute; left: 13px; top: 12px; color: var(--orange); font-family: "PT Sans", sans-serif; font-size: 26.5px; line-height: 32px; }
  .hero-rule { position: absolute; left: 11px; top: 79px; width: 260px; height: 1px; background: #888; }
  .hero-text { position: absolute; left: 18px; top: 95px; width: 310px; color: var(--white); font-size: 13px; line-height: 22px; }
  .hero-button { position: absolute; left: 24px; top: 295px; width: 238px; height: 48px; border-radius: 8px; background: linear-gradient(#f99a2e, var(--orange-dark)); border: 1px solid #b95400; color: var(--white); font-family: "PT Sans", sans-serif; font-weight: 700; font-size: 20px; line-height: 46px; padding-left: 8px; }
  .page-curl { position: absolute; right: 0; top: 0; }

  .card { top: 536px; width: 301px; height: 284px; background: var(--white); border: 1px solid var(--card-border); border-radius: 18px; box-shadow: inset 0 40px 40px -30px #f1f1f1; }
  .card-title { position: absolute; left: 22px; top: 14px; font-family: "PT Sans", sans-serif; font-weight: 700; font-size: 22px; }
  .card-title.orange { color: var(--orange); }
  .card-title.blue { color: var(--blue); }
  .card-photo { position: absolute; left: 19px; top: 50px; width: 258px; height: 130px; }
  .card-text { position: absolute; left: 19px; top: 189px; width: 258px; font-size: 11.5px; line-height: 20px; text-align: justify; letter-spacing: .4px; }
  .card-text b { font-weight: 700; }
  .view-more { position: absolute; left: 180px; top: 265px; width: 88px; height: 24px; background: linear-gradient(#fff, #e3e3e3); border-radius: 10px 10px 0 0; color: var(--blue); font-size: 11px; font-weight: 700; text-align: center; line-height: 24px; }
  .view-more::before, .view-more::after { content: ""; position: absolute; bottom: -6px; width: 14px; height: 10px; background: #333; border-radius: 0 0 8px 8px; }
  .view-more::before { left: -14px; } .view-more::after { right: -14px; }
  .video { position: absolute; left: 20px; top: 52px; width: 274px; height: 204px; background: #111; }
  .video-scene { position: absolute; left: 0; top: 18px; width: 274px; height: 162px; background: linear-gradient(135deg, #3b342e, #6d645b 50%, #2a2622); }
  .video-top { position: absolute; right: 6px; top: 4px; color: #ddd; font-size: 7px; }
  .video-bar { position: absolute; left: 0; bottom: 0; width: 274px; height: 22px; background: #1a1a1a; border-top: 3px solid #c00; }
  .video-play { position: absolute; left: 114px; top: 78px; width: 46px; height: 32px; border-radius: 6px; background: rgba(0,0,0,.8); }

  .site-footer { left: 0; top: 875px; width: 1200px; height: 100px; background: var(--footer-blue); border-top: 3px solid #0b3f78; }
  .footer-links { position: absolute; left: 113px; top: 24px; color: var(--white); font-family: "Open Sans", sans-serif; font-size: 12.5px; word-spacing: 2px; }
  .footer-links span { margin: 0 11px; }
  .copyright { position: absolute; left: 113px; top: 46px; color: var(--white); font-family: "Open Sans", sans-serif; font-size: 13px; }
  .connect { left: 872px; top: 865px; width: 202px; height: 93px; background: linear-gradient(#fff, #e4e4e4); border-radius: 0 0 10px 10px; box-shadow: 0 2px 6px rgba(0,0,0,.3); }
  .connect-title { position: absolute; left: 15px; top: 10px; font-family: "PT Sans", sans-serif; font-weight: 700; font-size: 22px; color: #444; letter-spacing: .5px; }
  .social { position: absolute; top: 44px; width: 32px; height: 32px; border-radius: 5px; }
</style>
</head>
<body>
  <header class="abs site-header">
    <div class="abs brand"><span class="brand-name">Youthful Hands</span><span class="brand-mark"></span></div>
    <div class="abs call-tab">
      <span class="call-icon"><svg width="14" height="16" viewBox="0 0 14 16"><path d="M3 1 L6 1 L6 5 L4 6 Q5 10 8 11 L9 9 L13 10 L13 14 Q8 15 4 11 Q1 7 3 1Z" fill="#fff"/></svg></span>
      <span class="call-label">Call us:</span><span class="call-number">555-318-2704</span>
    </div>
  </header>

  <nav class="abs main-nav">
    <a class="nav-link active" style="left:117px">Home</a>
    <span class="nav-sep" style="left:191px"></span><a class="nav-link" style="left:215px">Donate</a>
    <span class="nav-sep" style="left:287px"></span><a class="nav-link" style="left:313px">Become A Sponsor</a>
    <span class="nav-sep" style="left:455px"></span><a class="nav-link" style="left:480px">History</a>
    <span class="nav-sep" style="left:553px"></span><a class="nav-link" style="left:578px">News</a>
    <span class="nav-sep" style="left:641px"></span><a class="nav-link" style="left:665px">Contact Us</a>
  </nav>

  <div class="abs content-bg"></div>

  <section class="abs hero"></section>
  <div class="abs hero-photo" role="img" aria-label="Group of teenagers in matching white T-shirts at a fundraising stand"></div>
  <div class="abs hero-caption">Support each other, the environment and the poor, through fund raising and other philanthropic</div>
  <div class="abs hero-panel">
    <h1 class="hero-title">HELPING OTHERS<br>AROUND THE WORLD</h1>
    <div class="hero-rule"></div>
    <p class="hero-text"><b>During the summer of 2010</b>, a group of teens from Stone Harbor, NJ wanted to do something to help with the disaster in the Gulf.&nbsp; They raised thousands of dollars and 100% of the money was donated to help save animals.&nbsp; Sponsors funded the administration costs.&nbsp; It was a huge success and as a with final U.S. Government approval in November of 2011.</p>
    <a class="hero-button">Learn More, Click Here ›</a>
    <svg class="page-curl" width="112" height="62" viewBox="0 0 112 62">
      <path d="M0 0 H112 V62 Z" fill="#1d5fa8"/>
      <path d="M0 0 L112 62 Q80 64 60 44 Q40 22 0 0Z" fill="#d9d9d9"/>
      <path d="M0 0 Q40 22 60 44 Q50 20 0 0Z" fill="#f4f4f4"/>
    </svg>
  </div>

  <article class="abs card" style="left:146px">
    <h2 class="card-title orange">Disaster Relief</h2>
    <div class="card-photo" role="img" aria-label="Teens collecting donations under a tent" style="background:linear-gradient(135deg,#d8cbb8,#8b7a6a 50%,#e39a3c)"></div>
    <p class="card-text"><b>Playcrate is a amazing 30 Foot Long Mobile Multiplayer Gaming</b> Theater where "We Bring It" to you!</p>
    <a class="view-more">View more[+]</a>
  </article>
  <article class="abs card" style="left:462px">
    <h2 class="card-title blue">Environment</h2>
    <div class="card-photo" role="img" aria-label="Teen volunteer working at a laptop on a table" style="background:linear-gradient(135deg,#8c8c88,#d8d5cf 50%,#5d6a7a)"></div>
    <p class="card-text"><b>Playcrate is a amazing 30 Foot Long Mobile Multiplayer Gaming</b> Theater where "We Bring It" to you!</p>
    <a class="view-more">View more[+]</a>
  </article>
  <article class="abs card" style="left:779px">
    <h2 class="card-title blue">Featured Video</h2>
    <div class="video">
      <span class="video-top">Share &nbsp;&nbsp; ▾ More info</span>
      <div class="video-scene" role="img" aria-label="Video still of children watching a screen"></div>
      <span class="video-play"><svg width="46" height="32"><path d="M18 10 L30 16 L18 22Z" fill="#fff"/></svg></span>
      <div class="video-bar"><svg width="274" height="19"><path d="M10 6 L16 9.5 L10 13Z" fill="#ccc"/><rect x="38" y="7" width="6" height="6" fill="#ccc"/><text x="58" y="13" fill="#ccc" font-size="7" font-family="Arial">0:00</text></svg></div>
    </div>
  </article>

  <footer class="abs site-footer">
    <div class="footer-links">Home<span>|</span>Donate<span>|</span>Become A Sponsor<span>|</span>History<span>|</span>News<span>|</span>Contact Us</div>
    <div class="copyright">©1998-2012, Youthfulhands.com Inc. All Rights Reserved. Legal | Site Map</div>
  </footer>
  <aside class="abs connect">
    <h3 class="connect-title">Connect Us</h3>
    <span class="social" style="left:15px;background:#f39a1c" aria-label="Feed"></span>
    <span class="social" style="left:62px;background:#e9e9e9;border:1px solid #bbb"><svg width="30" height="30"><rect x="5" y="9" width="20" height="13" fill="none" stroke="#999"/><path d="M5 9 L15 17 L25 9" fill="none" stroke="#999"/></svg></span>
    <span class="social" style="left:108px;background:#3b5b9a" aria-label="Social network"></span>
    <span class="social" style="left:155px;background:#3fa3c8" aria-label="Social network"></span>
  </aside>
</body>
</html>
```